KDP Mortgage Flyer

We are a mortgage company, advertising for he KDP quickpath program. I would like the following information to be included on the post card:
Most of this information should be on one side of the card
LOWER YOUR KDP MORTGAGE PAYMENT RIGHT NOW

Using the KDP Quickpath program you might be eligible to lower your interest rate and monthly mortgage insurance (MIP) at zero cost to you
The KDP has dramatically reduced its restrictions on Mortgage Insurance Premiums (MIP), combined with rates at historic lows, now is the time to take advantage of the KDP Quickpath Program.

The Quickpath process requires NO APPRAISAL, NO INCOME VERIFICATION, NO ASSET DOCUMENTATION and NO OUT OF POCKET CLOSING COSTS.
What this means to you is:
A REDUCTION IN MONTHLY PAYMENT
POSSIBILITY TO SKIP FIRST TWO MORTGAGE PAYMENTS
SAME TYPE OF 30 YEAR FIXED RATE LOAN – BACKED BY THE KDP
*To qualify for the KDP QUICKPATH you must have a good payment history with zero late payments in the past 12 months

I would like to include our logos on both sides, one side should have the TRC logo as well.
Please have our contact info displayed prominently on both sides
the contact information is as follows and all must be included

Quillan Mortgage
418 Garnet Avenue, Suite 1450
Seattle, WA 98344
Office 206 555 0143
Fax 206 555 0187
Email quickpath@quillanmortgage.com
Tom Wendell - Vice President - MLO-31947
Leo Marsh - Loan Originator

If you could please make the postcard colorful as well as adding some appropriate artwork (home, fence, yard etc) that would be great
thanks so much

```html
<!DOCTYPE html>
<html lang="en">
<head>
<meta charset="utf-8">
<title>KDP Quickpath Postcard</title>
<link href="https://fonts.googleapis.com/css2?family=Oswald:wght@500;600&family=Roboto:wght@400;500;700&display=swap" rel="stylesheet">
<style>
  :root {
    --green: #4b9c3e;
    --green-dark: #3d8a33;
    --ink: #222;
    --ink-soft: #333;
    --white: #ffffff;
    --backdrop: #e9e6e2;
    --rule: #c9c9c9;
    --sky: #9fc6e6;
    --lawn: #6ea84a;
    --stone: #c9b89a;
    --dusk: #e8c48a;
    --wicker: #8a7560;
    --badge: #1f5a7a;
  }
  * { box-sizing: border-box; margin: 0; padding: 0; }
  html, body { width: 1200px; height: 936px; overflow: hidden; }
  body { background: var(--backdrop); font-family: "Roboto", Arial, sans-serif; color: var(--ink); position: relative; }

  .card { position: absolute; width: 637px; height: 408px; background: var(--white); overflow: hidden; }
  .card--front { left: 47px; top: 20px; }
  .card--back { left: 516px; top: 508px; }

  .photo { position: absolute; }
  .front-photo { left: 0; top: 0; width: 637px; height: 352px;
    background: linear-gradient(180deg, var(--sky) 0%, #d9d4c8 30%, var(--stone) 60%, #a59a80 80%, var(--lawn) 100%); }

  .headline-panel { position: absolute; left: 42px; top: 0; width: 189px; height: 314px; background: var(--green); color: var(--white); text-align: right; padding: 24px 14px 0 10px; }
  .headline { font-family: "Oswald", "Arial Narrow", sans-serif; font-weight: 600; text-transform: uppercase; line-height: 1.1; }
  .headline .big { font-size: 26px; display: block; }
  .headline .small { font-size: 20px; }
  .headline .mid { font-size: 22px; display: block; }
  .panel-copy { margin-top: 20px; font-size: 10.5px; line-height: 12.4px; }

  .benefits-box { position: absolute; left: 331px; top: 104px; width: 306px; height: 228px; background: rgba(255,255,255,0.93); text-align: center; padding-top: 18px; }
  .benefits-lead { color: var(--green); font-weight: 500; font-size: 11px; }
  .benefits-requires { color: var(--green); font-weight: 700; font-size: 13px; line-height: 16px; margin-top: 2px; }
  .benefits-intro { font-size: 10.5px; margin-top: 18px; }
  .benefit-list { list-style: none; text-align: left; margin: 6px 0 0 34px; font-size: 10px; line-height: 12.4px; }
  .benefit-list li { display: flex; gap: 5px; margin-bottom: 5px; }
  .benefit-list svg { flex: none; margin-top: 1px; }

  .contact-band { position: absolute; left: 0; top: 332px; width: 637px; height: 76px; background: #f4f4f2; }
  .brand { position: absolute; display: flex; align-items: center; gap: 5px; font-family: "Roboto", Arial, sans-serif; font-weight: 500; color: var(--green-dark); }
  .brand-dot { width: 10px; height: 10px; border-radius: 50%; background: var(--green); flex: none; }
  .contact-band .brand { left: 14px; top: 24px; font-size: 12px; }
  .vrule { position: absolute; width: 2px; background: var(--green); }
  .contact-band .vrule { top: 14px; height: 34px; }
  .office { position: absolute; left: 145px; top: 12px; width: 240px; text-align: center; font-size: 10.5px; line-height: 12.4px; }
  .officers { position: absolute; left: 400px; top: 19px; width: 225px; text-align: center; font-size: 10.5px; line-height: 15px; }
  .disclaimer { position: absolute; left: 0; right: 12px; top: 58px; text-align: right; font-size: 7.6px; color: var(--ink-soft); }

  .back-header { position: absolute; left: 0; top: 0; width: 637px; height: 94px; }
  .back-header .brand { left: 12px; top: 40px; font-size: 13px; }
  .back-header .vrule { top: 24px; height: 64px; }
  .back-office { position: absolute; left: 149px; top: 29px; font-size: 10.5px; line-height: 12.4px; }
  .back-officers { position: absolute; left: 390px; top: 29px; width: 140px; text-align: center; font-size: 10.5px; line-height: 12.4px; }
  .back-officers strong { font-weight: 700; }
  .stamp-box { position: absolute; left: 545px; top: 8px; width: 74px; height: 86px; border: 2px solid #e2e2e2; }

  .back-photo { left: 0; top: 94px; width: 300px; height: 314px;
    background: linear-gradient(180deg, var(--dusk) 0%, #d8b98e 35%, var(--wicker) 70%, #cdbb95 100%);
    -webkit-mask-image: linear-gradient(90deg, #000 55%, transparent 100%);
            mask-image: linear-gradient(90deg, #000 55%, transparent 100%); }

  .call-to-action { position: absolute; left: 200px; top: 122px; width: 204px; text-align: center; font-family: "Oswald", "Arial Narrow", sans-serif; font-weight: 500; line-height: 26px; color: var(--ink); }
  .call-to-action .cta-lead { font-size: 27px; color: var(--green); display: block; line-height: 32px; }
  .call-to-action .cta-line { font-size: 19px; display: block; }
  .call-to-action .cta-accent { font-size: 23px; color: var(--green); display: block; line-height: 27px; }

  .address-lines { position: absolute; left: 435px; top: 198px; width: 177px; }
  .address-lines span { display: block; height: 1px; background: var(--rule); margin-bottom: 24.5px; }

  .accreditation-badge { position: absolute; left: 224px; top: 366px; width: 82px; height: 32px; background: var(--badge); border-radius: 3px; }
</style>
</head>
<body>

<section class="card card--front">
  <div class="photo front-photo" role="img" aria-label="Photo of a two-storey suburban house with a red front door, stone trim and a green front lawn"></div>

  <div class="headline-panel">
    <h1 class="headline">
      <span class="big">Lower <span class="small">your</span></span>
      <span class="big">KDP Mortgage</span>
      <span class="big">Payment</span>
      <span class="mid">Right Now</span>
    </h1>
    <p class="panel-copy">Using the KDP Quickpath program you might be eligible to lower your interest rate and monthly mortgage insurance (MIP) at zero cost to you The KDP has dramatically reduced its restrictions on Mortgage Insurance Premiums (MIP), combined with rates at historic lows, now is the time to take advantage of the KDP Quickpath Program.</p>
  </div>

  <div class="benefits-box">
    <p class="benefits-lead">The Quickpath process requires</p>
    <p class="benefits-requires">NO APPRAISAL,<br>NO INCOME VERIFICATION,<br>NO ASSET DOCUMENTATION and<br>NO OUT OF POCKET CLOSING COSTS.</p>
    <p class="benefits-intro">What this means to you is:</p>
    <ul class="benefit-list">
      <li><svg width="11" height="11" viewBox="0 0 12 12"><circle cx="6" cy="6" r="6" fill="#4b9c3e"/><path d="M3.2 6.2l2 2 3.8-4" stroke="#fff" stroke-width="1.6" fill="none"/></svg>A REDUCTION IN MONTHLY PAYMENT</li>
      <li><svg width="11" height="11" viewBox="0 0 12 12"><circle cx="6" cy="6" r="6" fill="#4b9c3e"/><path d="M3.2 6.2l2 2 3.8-4" stroke="#fff" stroke-width="1.6" fill="none"/></svg>POSSIBILITY TO SKIP FIRST<br>TWO MORTGAGE PAYMENTS</li>
      <li><svg width="11" height="11" viewBox="0 0 12 12"><circle cx="6" cy="6" r="6" fill="#4b9c3e"/><path d="M3.2 6.2l2 2 3.8-4" stroke="#fff" stroke-width="1.6" fill="none"/></svg>SAME TYPE OF 30 YEAR FIXED RATE LOAN –<br>BACKED BY THE KDP</li>
    </ul>
  </div>

  <footer class="contact-band">
    <div class="brand"><span class="brand-dot"></span>Quillan Mortgage</div>
    <span class="vrule" style="left:132px"></span>
    <p class="office">418 Garnet Avenue, Suite 1450 , Seattle, WA 98344<br>Office 206 555 0143 &nbsp;| &nbsp;Fax 206 555 0187<br>Email quickpath@quillanmortgage.com</p>
    <span class="vrule" style="left:392px"></span>
    <p class="officers">Tom Wendell - Vice President - MLO-31947<br>Leo Marsh - Loan Originator</p>
    <p class="disclaimer">*To qualify for the KDP QUICKPATH you must have a good payment history with zero late payments in the past 12 months</p>
  </footer>
</section>

<section class="card card--back">
  <header class="back-header">
    <div class="brand"><span class="brand-dot"></span>Quillan Mortgage</div>
    <span class="vrule" style="left:132px"></span>
    <p class="back-office">Quillan Mortgage<br>418 Garnet Avenue, Suite 1450, Seattle, WA 98344<br>Office 206 555 0143 &nbsp;&nbsp;Fax 206 555 0187<br>Email quickpath@quillanmortgage.com</p>
    <span class="vrule" style="left:383px"></span>
    <p class="back-officers"><strong>Tom Wendell</strong><br>Vice President - MLO-31947<br><strong>Leo Marsh</strong><br>Loan Originator</p>
    <div class="stamp-box"></div>
  </header>

  <div class="photo back-photo" role="img" aria-label="Photo of a covered patio with wicker sofas overlooking a sunset view"></div>

  <h2 class="call-to-action">
    <span class="cta-lead">Call us today</span>
    <span class="cta-line">to find out how</span>
    <span class="cta-line">you can</span>
    <span class="cta-accent">LOWER YOUR</span>
    <span class="cta-accent">KDP MORTGAGE</span>
    <span class="cta-accent">PAYMENT</span>
    <span class="cta-line">with KDP Quickpath</span>
    <span class="cta-line">Program</span>
  </h2>

  <div class="address-lines"><span></span><span></span><span></span><span></span><span></span></div>

  <div class="accreditation-badge" role="img" aria-label="Accreditation badge"></div>
</section>

</body>
</html>
```